Velisto Events Business Card

We need a business cards that stands out to our clients. We are company who targets prestige clients to spend money with us on experiences, so our image needs to be prestige
Target Market(s)
Corporate
Contact Information for Business Card
There will be four different names on the business cards
Dana Morrowby
Director
O: 02 5147 3086
M: 0451 692 038
E: info@velistoevents.example.au
Facebook: @velistoevents
Instagram: velistoevents
www.velistoevents.example.au
Nathaniel Morrowby
Director
O: 02 5147 3086
M: 0467 215 904
Facebook: @velistoevents
Instagram: velistoevents
www.velistoevents.example.au
Teodor Vinkel
Director
O: 02 5147 3086
M: 0478 903 527
Facebook: @velistoevents
Instagram: velistoevents
www.velistoevents.example.au
Mabel Hartung
Director
O: 02 5147 3086
Facebook: @velistoevents
Instagram: velistoevents
www.velistoevents.example.au
Colors
Designer to choose colors to be used in the design.
Look and feel

```html
<!DOCTYPE html>
<html lang="en">
<head>
<meta charset="utf-8">
<title>Velisto Events Business Card</title>
<link rel="stylesheet" href="https://fonts.googleapis.com/css2?family=Cinzel:wght@400;500&family=Cormorant+Garamond:ital,wght@1,600&family=Open+Sans:wght@400&display=swap">
<style>
  :root {
    --page: #ece8e1;
    --navy: #2b2664;
    --navy-deep: #221d52;
    --navy-light: #3a3478;
    --gold: #d8b45e;
    --white: #ffffff;
    --edge: #cfcbd8;
  }
  * { margin: 0; padding: 0; box-sizing: border-box; }
  html, body {
    width: 1200px;
    height: 800px;
    overflow: hidden;
    background: var(--page);
  }
  .canvas {
    position: relative;
    width: 1200px;
    height: 800px;
  }
  .card {
    position: absolute;
    left: 340px;
    width: 520px;
    height: 296px;
    border-radius: 14px;
    overflow: hidden;
    background: radial-gradient(ellipse at 60% 55%, var(--navy-light) 0%, var(--navy) 55%, var(--navy-deep) 100%);
    box-shadow: 0 0 0 1px var(--edge), 0 6px 14px rgba(0,0,0,0.18);
  }
  .card--front { top: 74px; }
  .card--back { top: 420px; }

  /* front */
  .brand {
    position: absolute;
    left: 70px;
    top: 112px;
    width: 170px;
    text-align: center;
    font-family: "Cinzel", serif;
    font-weight: 500;
    color: var(--gold);
  }
  .brand__mark {
    display: block;
    width: 14px;
    height: 14px;
    margin: 0 auto 14px;
    border-radius: 50%;
    background: var(--gold);
  }
  .brand__name {
    display: block;
    font-size: 19px;
    letter-spacing: 5px;
    line-height: 1.1;
  }
  .brand__sub {
    display: block;
    font-size: 10px;
    letter-spacing: 4px;
    margin-top: 3px;
  }
  .person {
    position: absolute;
    left: 282px;
    top: 92px;
  }
  .person__name {
    font-family: "Cinzel", serif;
    font-weight: 400;
    font-size: 19px;
    color: var(--white);
    letter-spacing: 0.5px;
  }
  .person__title {
    font-family: "Cormorant Garamond", serif;
    font-style: italic;
    font-weight: 600;
    font-size: 13px;
    color: var(--gold);
    margin: 2px 0 12px;
  }
  .contact {
    list-style: none;
    font-family: "Open Sans", sans-serif;
    font-size: 11.5px;
    color: var(--white);
  }
  .contact li {
    display: flex;
    align-items: center;
    gap: 7px;
    height: 22px;
  }
  .contact svg { width: 11px; height: 11px; flex: none; }

  /* back */
  .crest-pattern {
    position: absolute;
    inset: 0;
    background: linear-gradient(135deg, rgba(255,255,255,0.03), rgba(0,0,0,0.05));
  }
  .wordmark {
    position: absolute;
    left: 0;
    right: 0;
    top: 118px;
    text-align: center;
    font-family: "Cinzel", serif;
    font-weight: 500;
    color: var(--gold);
  }
  .wordmark__name {
    display: block;
    font-size: 30px;
    letter-spacing: 10px;
    line-height: 1;
  }
  .wordmark__sub {
    display: block;
    font-size: 15px;
    letter-spacing: 5px;
    margin-top: 6px;
  }
</style>
</head>
<body>
<main class="canvas">

  <section class="card card--front" aria-label="Business card front">
    <div class="brand">
      <span class="brand__mark"></span>
      <span class="brand__name">VELISTO</span>
      <span class="brand__sub">EVENTS</span>
    </div>
    <div class="person">
      <h1 class="person__name">YOUR NAME</h1>
      <p class="person__title">Job Title</p>
      <ul class="contact">
        <li>
          <svg viewBox="0 0 12 12" aria-hidden="true"><rect x="3" y="0.8" width="6" height="10.4" rx="1" fill="none" stroke="#fff" stroke-width="1"/><line x1="5" y1="9.6" x2="7" y2="9.6" stroke="#fff" stroke-width="0.8"/></svg>
          000 000 0000
        </li>
        <li>
          <svg viewBox="0 0 12 12" aria-hidden="true"><rect x="0.5" y="2.5" width="11" height="7.5" fill="#d8b45e"/><polyline points="0.5,2.5 6,7 11.5,2.5" fill="none" stroke="#2b2664" stroke-width="0.9"/></svg>
          youremail@example.com
        </li>
        <li>
          <svg viewBox="0 0 12 12" aria-hidden="true"><circle cx="6" cy="6" r="5" fill="none" stroke="#fff" stroke-width="0.9"/><ellipse cx="6" cy="6" rx="2.2" ry="5" fill="none" stroke="#fff" stroke-width="0.8"/><line x1="1" y1="6" x2="11" y2="6" stroke="#fff" stroke-width="0.8"/></svg>
          www.yourwebsite.example
        </li>
      </ul>
    </div>
  </section>

  <section class="card card--back" aria-label="Business card back">
    <div class="crest-pattern" role="img" aria-label="Faint repeating crest pattern in tone-on-tone navy"></div>
    <div class="wordmark">
      <span class="wordmark__name">VELISTO</span>
      <span class="wordmark__sub">EVENTS</span>
    </div>
  </section>

</main>
</body>
</html>
```